依頼詳細
米袋パッケージデザインの依頼をさせて頂きます。
今回、特に希望する方向性はございません。

自由度がかなり高く、曖昧な部分がある為デザインが難しいかと思われますが、
どうか力をお貸しください。

・高級感、シンプルさ、オシャレな感じ、ポップな感じ、
そよ凪や宵月の調べ・岳兵衛などの統一デザインっぽさ、
など方向性は自由です。
・洋風、和風など自由です。
・写真、イラスト、フォント自由です。筆文字可。(版権等にご注意ください。)
・色も自由です。金色銀色使用可能です。

良いと思うデザイン例
・コンセプトやデザインに一捻りあるもの。
(絶対に必要というわけではありません。)
・特別感。(絶対に必要というわけではありません。)

悪いと思うデザイン例
・スーパーによく置いてあるような安っぽい感じ。

■デザイン上に必ず入れて欲しいもの■
※すべて「」は必要ありません。

・「新潟県産」※新潟や新潟産でもかまいません。
・「こしひかり」※カタカナでもかまいません。
・「5kg」
・「中のお米が見える部分」

印刷適正・文字などはデザイン決定後こちらで調整致しますので
背景や全体のデザインイメージを重要視します。

・修正作業をお願いすることはありません。
・ご提案をして頂く際に、袋に印刷されたように見える
擬似実物処理(立体)などは不要です。
平面画像のみで公平に判断したいと考えております。
記載項目
サイズ:W300mm×H470mm
グラビア印刷/ラミネート加工

```html
<!DOCTYPE html>
<html lang="ja">
<head>
<meta charset="utf-8">
<title>こしひかり 5kg 米袋デザイン</title>
<link rel="stylesheet" href="https://fonts.googleapis.com/css2?family=Kaisei+Decol:wght@400;700&family=Shippori+Mincho:wght@600&display=swap">
<style>
  :root {
    --paper: #ffffff;
    --gold: #b08a2a;
    --crimson: #c50f13;
    --ink: #3b2a0e;
    --rice-light: #f4f2ec;
    --rice-shade: #d9d5cc;
  }
  html, body {
    margin: 0;
    padding: 0;
    overflow: hidden;
    background: var(--paper);
  }
  .rice-bag {
    position: relative;
    width: 766px;
    height: 1200px;
    overflow: hidden;
    background: var(--paper);
  }
  .rice-bag__layer {
    position: absolute;
    inset: 0;
  }
  .cross-band {
    position: absolute;
    background: var(--gold);
  }
  .cross-band--vertical {
    left: 311px;
    width: 144px;
    top: 0;
    height: 1200px;
  }
  .cross-band--horizontal {
    left: 0;
    width: 766px;
    top: 472px;
    height: 110px;
  }
  .dot {
    position: absolute;
    width: 144px;
    height: 144px;
    border-radius: 50%;
    background: var(--gold);
    display: flex;
    align-items: center;
    justify-content: center;
  }
  .dot--top-left { left: 94px; top: 316px; }
  .dot--top-right { left: 520px; top: 316px; background: var(--crimson); }
  .dot--bottom-left { left: 94px; top: 630px; }
  .dot--bottom-right { left: 520px; top: 630px; }
  .weight-label {
    font-family: "Shippori Mincho", serif;
    font-weight: 600;
    font-size: 50px;
    color: var(--ink);
    letter-spacing: 1px;
  }
  .product-name {
    position: absolute;
    left: 311px;
    width: 144px;
    top: 235px;
    margin: 0;
    writing-mode: vertical-rl;
    font-family: "Kaisei Decol", serif;
    font-weight: 400;
    font-size: 112px;
    line-height: 144px;
    letter-spacing: 12px;
    color: var(--ink);
    text-align: start;
  }
  .origin-label {
    position: absolute;
    left: 50px;
    top: 500px;
    margin: 0;
    font-family: "Shippori Mincho", serif;
    font-weight: 600;
    font-size: 46px;
    line-height: 54px;
    letter-spacing: 2px;
    color: var(--ink);
  }
</style>
</head>
<body>
<main class="rice-bag">
  <svg class="rice-bag__layer rice-window" width="766" height="1200" viewBox="0 0 766 1200" role="img" aria-label="袋の中のお米が見える透明窓（上下の白米）">
    <defs>
      <radialGradient id="rice-grain" cx="50%" cy="50%" r="70%">
        <stop offset="0%" stop-color="var(--rice-light)"/>
        <stop offset="100%" stop-color="var(--rice-shade)"/>
      </radialGradient>
    </defs>
    <rect x="0" y="0" width="766" height="1200" fill="url(#rice-grain)"/>
  </svg>
  <svg class="rice-bag__layer label-field" width="766" height="1200" viewBox="0 0 766 1200" aria-hidden="true">
    <ellipse cx="383" cy="600" rx="533" ry="460" fill="var(--paper)"/>
  </svg>

  <div class="cross-band cross-band--vertical"></div>
  <div class="cross-band cross-band--horizontal"></div>

  <div class="dot dot--top-left"></div>
  <div class="dot dot--top-right"></div>
  <div class="dot dot--bottom-left"></div>
  <div class="dot dot--bottom-right"><span class="weight-label">5kg</span></div>

  <p class="origin-label">新潟産</p>
  <h1 class="product-name">こしひかり</h1>
</main>
</body>
</html>
```